Bright Canyon, LLC Business Card Design

We need a product business card designed for a new company Bright Canyon, LLC. We make and resell waterless RV cleaner, polish and protectant. It cleans and protects in a simple spray and wipe step leaving the surface protected and conditioned to repel dust, dirt, water, smudges, bugs and fingerprints while preventing fogging. Safe on acrylic, clarisheet, durvane, plastic, rubber, painted surfaces, chrome, stainless, aluminum, vinyl, leather, glass.... This is an eco-friendly green product.

We want to play off the company name to tell the consumer that the product is easy to use and associate to the nostalgics 1950's in the USA... Thinking old travel trailer with hot rod truck pulling it as the graphic, maybe the husband cleaning the truck and the wife cleaning the trailer for a Bright Canyon surface.
Updates

Just posted our newly finished logo. Need to have "Cleaner and Protectant" added to the design as well. Thanks everyone that has submitted thus far, i am working to get comments on all.

If you need a different file format, please let me know. Thank you.

Most important info, is the logo, website and the words "Cleaner" or "Clean" along "Protectant" or "Protect" the remainder is of less importance. Highlight: www.brightcanyoncleaner.example Focus is on company brand for Brighter Canyon Cleaner product: However, need a section for the following contact info: John Doe (xxx) xxx-xxxx email address Would like space for QR Code if possible.

Target Market(s)

Adults in the USA between ages of 35-75 that are actively involved in the Recreational Vehicle (RV), travel trailer, and hot rod lifestyle. We are targeting the RV marked of the high end travel, 5th wheel and bus RV market. Along with hot rods, automotive and motorcycle market.

Industry/Entity Type

Travel

Requirements
Must have
• Most important info, is the logo, website and the words "Cleaner" or "Clean" along "Protectant" or "Protect" the remainder is of less importance.

Highlight:
www.brightcanyoncleaner.example

Focus is on company brand for Brighter Canyon Cleaner product: However, need a section for the following contact info:

John Doe
(xxx) xxx-xxxx
email address
Nice to have
• Would like a space for a QR Code.

```html
<!DOCTYPE html>
<html lang="en">
<head>
<meta charset="utf-8">
<title>Bright Canyon, LLC — Business Card</title>
<link rel="stylesheet" href="https://fonts.googleapis.com/css2?family=Open+Sans:wdth,wght@75..100,400..700&display=swap">
<style>
  :root {
    --brand-blue: #0f6cbd;
    --ink: #1d1d1f;
    --paper: #ffffff;
    --paper-shade: #f4f4f5;
    --backdrop: #2b2b2d;
    --truck-red: #d9484c;
    --truck-grey: #d4d6d8;
    --qr-line: #9aa3ad;
  }
  * { box-sizing: border-box; margin: 0; padding: 0; }
  html, body {
    width: 1200px; height: 800px; overflow: hidden;
    background: var(--backdrop);
    font-family: "Open Sans", Arial, sans-serif;
  }
  .stage {
    width: 1200px; height: 800px;
    display: flex; align-items: center; justify-content: center; gap: 40px;
  }
  .card {
    position: relative;
    width: 540px; height: 309px;
    background: var(--paper);
    overflow: hidden;
  }
  .card-frame { position: absolute; inset: 0; width: 100%; height: 100%; }
  .card-frame .accent { fill: var(--brand-blue); }
  .card-frame .arc { fill: none; stroke: var(--brand-blue); stroke-width: 30; }

  /* front */
  .front-title {
    position: absolute; left: 0; right: 0; top: 26px;
    text-align: center;
    font-size: 42px; font-weight: 400; font-stretch: 75%;
    color: var(--brand-blue); line-height: 1.2;
  }
  .front-tagline {
    position: absolute; left: 0; right: 0; top: 84px;
    text-align: center;
    font-size: 15px; font-weight: 600; letter-spacing: 1.5px;
    text-transform: uppercase; color: var(--ink);
  }
  .front-artwork {
    position: absolute; left: 150px; top: 114px; width: 240px; height: 148px;
    border-radius: 18px;
    background: linear-gradient(160deg, var(--truck-red) 0%, #e88a8c 45%, var(--truck-grey) 100%);
  }
  .front-website {
    position: absolute; left: 0; right: 0; top: 270px;
    text-align: center;
    font-size: 14px; font-weight: 700; color: var(--brand-blue);
  }

  /* back */
  .back { background: var(--paper-shade); }
  .holder { position: absolute; left: 30px; top: 110px; }
  .holder-name { font-size: 17px; font-weight: 700; color: var(--ink); line-height: 1.1; }
  .holder-role { font-size: 11px; color: var(--brand-blue); line-height: 1.2; }
  .holder-company {
    font-size: 30px; font-weight: 400; font-stretch: 75%;
    color: var(--brand-blue); line-height: 1.1; margin-top: 2px;
  }
  .qr-space {
    position: absolute; left: 368px; top: 70px; width: 76px; height: 76px;
    border: 2px dashed var(--qr-line); background: var(--paper);
  }
  .contact-list { position: absolute; list-style: none; font-size: 12.5px; color: var(--ink); }
  .contact-list li { display: flex; align-items: center; gap: 8px; height: 26px; white-space: nowrap; }
  .contact-list svg { width: 13px; height: 13px; fill: var(--brand-blue); flex: none; }
  .contact-phones { left: 34px; top: 204px; }
  .contact-online { left: 178px; top: 204px; }
</style>
</head>
<body>
<main class="stage">

  <section class="card front" aria-label="Card front">
    <svg class="card-frame" viewBox="0 0 540 309" aria-hidden="true">
      <path class="accent" d="M0 0H96V16H16V86H0Z"/>
      <path class="accent" d="M540 309H444V293H524V223H540Z"/>
    </svg>
    <h1 class="front-title">Bright Canyon, LLC</h1>
    <p class="front-tagline">Cleaner and Protectant</p>
    <div class="front-artwork" role="img" aria-label="Illustration of a red pickup truck with a roof rack"></div>
    <p class="front-website">www.brightcanyoncleaner.example</p>
  </section>

  <section class="card back" aria-label="Card back">
    <svg class="card-frame" viewBox="0 0 540 309" aria-hidden="true">
      <path class="accent" d="M0 0H96V16H16V86H0Z"/>
      <path class="accent" d="M0 309H96V293H16V223H0Z"/>
      <path class="arc" d="M300 15H375A150 150 0 0 1 525 165V309"/>
    </svg>

    <div class="holder">
      <p class="holder-name">Dale Warren</p>
      <p class="holder-role">Manager</p>
      <p class="holder-company">Bright Canyon, LLC</p>
    </div>

    <div class="qr-space" role="img" aria-label="Space reserved for a QR code"></div>

    <ul class="contact-list contact-phones">
      <li><svg viewBox="0 0 24 24"><path d="M6.6 10.8a15.1 15.1 0 0 0 6.6 6.6l2.2-2.2c.3-.3.7-.4 1-.2 1.1.4 2.300.6 3.600.6.6 0 1 .4 1 1V20c0 .6-.4 1-1 1A17 17 0 0 1 3 4c0-.6.4-1 1-1h3.5c.6 0 1 .4 1 1 0 1.3.2 2.5.6 3.6.1.3 0 .7-.2 1z"/></svg>555-014-2790</li>
      <li><svg viewBox="0 0 24 24"><path d="M6.6 10.8a15.1 15.1 0 0 0 6.6 6.6l2.2-2.2c.3-.3.7-.4 1-.2 1.1.4 2.3.6 3.6.6.6 0 1 .4 1 1V20c0 .6-.4 1-1 1A17 17 0 0 1 3 4c0-.6.4-1 1-1h3.5c.6 0 1 .4 1 1 0 1.3.2 2.5.6 3.6.1.3 0 .7-.2 1z"/></svg>555-014-2791</li>
    </ul>

    <ul class="contact-list contact-online">
      <li><svg viewBox="0 0 24 24"><path d="M2 5h20v14H2zm2 2v.5l8 5 8-5V7z"/></svg>hello@brightcanyon.example</li>
      <li><svg viewBox="0 0 24 24"><path d="M12 2a7 7 0 0 0-7 7c0 5 7 13 7 13s7-8 7-13a7 7 0 0 0-7-7zm0 9.5A2.5 2.5 0 1 1 12 6.5a2.5 2.5 0 0 1 0 5z"/></svg>4820 Juniper Lane Cedar Hollow, CA 90000</li>
      <li><svg viewBox="0 0 24 24"><path d="M12 2a10 10 0 1 0 0 20 10 10 0 0 0 0-20zm0 2c.9 1.2 1.6 2.6 2 4h-4c.4-1.4 1.1-2.8 2-4zM4.3 14a8 8 0 0 1 0-4h3.5a16 16 0 0 0 0 4zm.9 2h3c.4 1.4 1 2.7 1.8 3.8A8 8 0 0 1 5.2 16zm3-8h-3a8 8 0 0 1 4.8-3.8C9.2 5.3 8.6 6.6 8.2 8zM12 20c-.9-1.2-1.6-2.6-2-4h4c-.4 1.4-1.1 2.8-2 4zm2.3-6H9.7a14 14 0 0 1 0-4h4.6a14 14 0 0 1 0 4zm.2 5.8c.8-1.1 1.4-2.4 1.8-3.8h3a8 8 0 0 1-4.8 3.8zM16.2 14a16 16 0 0 0 0-4h3.5a8 8 0 0 1 0 4z"/></svg>www.brightcanyoncleaner.example</li>
    </ul>
  </section>

</main>
</body>
</html>
```